Voranel.com Personal Trainer/Fitness Website

I want a website to market my personal training/Outdoor Bootcamp Class services, as well as to ditribute nutrivexa. I need a logo as well I included an address for the Harbor Gales 1975 logo. I'd like Voranel in place of Harbor Gales, and in Black and white, just different enough so I can't get sued by the PLX.
https://www.pictofind.example/imgres?imgurl=http%3A%2F%2Fwww.dorian-halverstock.example%2Fwp-content%2Fuploads%2F2014%2F01%2Fgales_mark4.jpg&imgrefurl=http%3A%2F%2Fwww.dorian-halverstock.example%2Fplx-emblem-reworks-tulsa-harbor-bolts%2F&docid=_qweRT8uPLmnBx&tbnid=k3tyA7XbNqwePZ%3A&w=600&h=450&client=ms-android-carrierx&bih=512&biw=360&ved=0ahUKEwiQazxcv7LMAhUTwGMKHRPMBWMQMwg6KBQwFA&iact=mrc&uact=8.
It should be about 5 pages 1. home 2. about 3. Services 4. Blog/Videos and programs 5. Contact.
http://www.tobenwelfitness.example.uk/ is a website I like the style of.

Target Market(s)

Seattle area

Industry/Entity Type

Fitness

Coding

Coded - Design and coding required

Number of Pages Required

4 page

Font styles to use
Serif
Sans Serif

Requirements
Must have
• A minimal look
Nice to have
• A logo similar to the 1975 Harbor Galewinds Logo, with a Small Dorn Velask ripping his shirt open(with a picture of the logo on his shirt, picture within picture) to turn into Skyvaler in the center. Skyline is black, Background and small figure white(with black logo on shirt)

```html
<!DOCTYPE html>
<html lang="en">
<head>
<meta charset="utf-8">
<title>Voranel.com — Personal Trainer</title>
<link rel="stylesheet" href="https://fonts.googleapis.com/css2?family=Roboto:wght@400;500;700&family=Roboto+Slab:wght@100;300;700&family=Ubuntu:wght@500;700&display=swap">
<style>
  :root{
    --black:#000;
    --ink:#0a0a0a;
    --red:#c8161d;
    --red-bright:#e02a33;
    --red-deep:#5a0a10;
    --white:#fff;
    --grey:#8a8a8a;
    --footer:#1b1b1b;
    --rule:#1e1e1e;
  }
  *{margin:0;padding:0;box-sizing:border-box}
  html,body{width:1073px;height:1200px;overflow:hidden;background:var(--black)}
  body{position:relative;font-family:"Roboto",sans-serif;color:var(--white)}
  .abs{position:absolute}

  /* header */
  .brand{left:218px;top:20px}
  .brand-name{font-family:"Ubuntu",sans-serif;font-weight:500;font-size:27px;color:var(--red-bright);line-height:1;letter-spacing:-.3px}
  .brand-tag{font-size:9.5px;color:var(--white);margin-top:2px;letter-spacing:.2px}
  .main-nav{left:490px;top:36px;display:flex;gap:0;font-size:9px;font-weight:700;text-transform:uppercase}
  .main-nav a{color:var(--white);text-decoration:none;position:absolute;white-space:nowrap}
  .main-nav sup,.foot-nav sup{font-size:4.5px;color:var(--red-bright);margin-right:1px;vertical-align:4px}

  /* hero */
  .hero{left:0;top:0;width:1073px;height:590px}
  .hero-title{left:530px;top:192px;display:flex;align-items:center}
  .hero-be{width:143px;height:89px;background:var(--white);color:var(--red-deep);font-family:"Roboto Slab",serif;font-weight:700;font-size:74px;display:flex;align-items:center;justify-content:center;letter-spacing:-2px}
  .hero-fit{font-family:"Roboto Slab",serif;font-weight:100;font-size:78px;color:var(--white);margin-left:19px;line-height:1}
  .hero-copy{left:530px;top:318px;font-size:11px;line-height:20px;color:#f2e6e6}
  .btn{display:flex;align-items:center;gap:12px;font-size:9px;font-weight:700;text-decoration:none;height:26px;padding:0 12px 0 13px}
  .btn::after{content:"";border-left:4px solid currentColor;border-top:3px solid transparent;border-bottom:3px solid transparent}
  .btn-red{background:var(--red);color:var(--white)}
  .btn-white{background:var(--white);color:var(--red)}
  .hero-btn{left:530px;top:388px;width:117px;justify-content:space-between}

  /* welcome */
  .welcome{left:216px;top:603px;width:276px}
  .welcome h1{font-family:"Ubuntu",sans-serif;font-weight:500;font-size:21px;color:var(--red-bright);margin-left:2px}
  .welcome p{font-size:7.6px;line-height:13.6px;margin-top:13px;color:#eee}
  .welcome .btn{width:129px;margin-top:18px;justify-content:space-between}

  .media{left:536px;top:608px;width:318px;height:154px}
  .media-gym{left:0;top:0;width:159px;height:154px;background:linear-gradient(180deg,#c9ccd0 0%,#8a8d90 45%,#b9894f 60%,#7a5530 100%)}
  .media-outdoor{left:159px;top:0;width:159px;height:77px;background:linear-gradient(180deg,#c9d6e2 0%,#7d9a6a 55%,#4d6b38 100%)}
  .play{left:272px;top:27px}
  .media-more{left:159px;top:77px;width:159px;height:77px;background:var(--red);font-size:8.8px;font-weight:700;line-height:14px;padding:29px 18px 0}

  /* numbers */
  .numbers{left:218px;top:844px;width:636px;height:138px;display:grid;grid-template-columns:repeat(4,1fr)}
  .num-cell{border-right:1px solid var(--rule);text-align:center;position:relative}
  .num-intro{text-align:left;overflow:hidden}
  .num-intro-photo{position:absolute;left:62px;top:0;width:97px;height:138px;background:radial-gradient(ellipse at 55% 40%,#3a2a25 0%,#181110 55%,#050505 100%)}
  .num-intro h2{position:absolute;left:0;top:66px;font-family:"Ubuntu",sans-serif;font-weight:700;font-size:19px;line-height:20px}
  .num-intro svg{position:absolute;left:0;top:21px}
  .num-value{font-family:"Roboto",sans-serif;font-weight:700;font-size:52px;color:var(--red);line-height:1;margin-top:20px;letter-spacing:-1px}
  .num-label{font-size:7.6px;line-height:13.6px;margin-top:14px;color:#ddd}

  /* blog band */
  .blog{left:218px;top:1028px;width:636px;height:67px;background:linear-gradient(90deg,var(--red) 0%,#c21a22 60%,#a3141b 100%)}
  .blog h2{left:22px;top:17px;font-family:"Ubuntu",sans-serif;font-weight:500;font-size:16.5px;line-height:17px}
  .blog p{left:141px;top:24px;font-size:7.6px;line-height:17px}
  .blog-art{left:390px;top:-20px;width:96px;height:84px;background:radial-gradient(ellipse at center,#d8d8d8 0%,#8d8d8d 45%,rgba(120,20,25,0) 72%)}
  .blog .btn{left:520px;top:19px;width:92px;justify-content:space-between}

  /* footer */
  .footer{left:218px;top:1134px;width:636px;height:66px;background:var(--footer)}
  .foot-nav{left:21px;top:28px;font-size:7.4px;font-weight:500;text-transform:uppercase;color:var(--grey)}
  .foot-nav a{color:var(--grey);text-decoration:none;position:absolute;white-space:nowrap}
  .copyright{right:24px;top:28px;font-size:7.4px;color:#5d5d5d;white-space:nowrap}
</style>
</head>
<body>

<section class="hero abs">
  <svg width="1073" height="590" viewBox="0 0 1073 590">
    <defs>
      <linearGradient id="band" x1="0" y1="0" x2="1" y2="0.3">
        <stop offset="0" stop-color="#4a0a0f"/>
        <stop offset=".55" stop-color="#b8202a"/>
        <stop offset="1" stop-color="#d64350"/>
      </linearGradient>
      <radialGradient id="athlete" cx=".5" cy=".45" r=".6">
        <stop offset="0" stop-color="#a34a3c"/>
        <stop offset=".55" stop-color="#5e1c18"/>
        <stop offset="1" stop-color="#1a0505" stop-opacity="0"/>
      </radialGradient>
    </defs>
    <rect width="1073" height="590" fill="#000"/>
    <polygon points="0,152 1073,60 1073,480 0,575" fill="url(#band)"/>
    <polygon points="0,470 1073,378 1073,392 0,484" fill="#e0404b" opacity=".45"/>
    <polygon points="0,430 1073,338 1073,344 0,436" fill="#ff6f7a" opacity=".3"/>
    <rect x="80" y="60" width="330" height="520" fill="url(#athlete)" role="img" aria-label="Photo of a muscular athlete sprinting forward"/>
  </svg>
</section>

<header>
  <div class="brand abs">
    <div class="brand-name">Voranel.com</div>
    <div class="brand-tag">Personal Trainer</div>
  </div>
  <nav class="main-nav abs">
    <a href="#" style="left:0"><sup>01</sup>Home</a>
    <a href="#" style="left:65px"><sup>02</sup>About</a>
    <a href="#" style="left:135px"><sup>03</sup>Services</a>
    <a href="#" style="left:214px"><sup>04</sup>Blog/Videos</a>
    <a href="#" style="left:313px"><sup>05</sup>Contact</a>
  </nav>
</header>

<div class="hero-title abs">
  <div class="hero-be">BE</div>
  <div class="hero-fit">FIT</div>
</div>
<p class="hero-copy abs">Aenean venenatis lacinia erat, vitae gravida risus tempus et.<br>Curabitur tempor metus quis nisi varius et sodales nisi dapibus.</p>
<a class="btn btn-red hero-btn abs" href="#">View my programs</a>

<section class="welcome abs">
  <h1>Welcome to my site</h1>
  <p>Mauris vel velit eget lorem sodales lobortis ut lacinia neque. Donec id cursus tortor. Nullam eget ligula sed augue aliquet pharetra.</p>
  <p>Aenean egestas vestibulum leo, eget fermentum odio dignissim a. Phasellus interdum massa vel arcu pharetra tristique. Sed et mi rhoncus tellus faucibus consequat pulvinar non quam.</p>
  <a class="btn btn-white" href="#">Check out my services</a>
</section>

<section class="media abs">
  <div class="media-gym abs" role="img" aria-label="Photo of an indoor gym with exercise balls and a wooden floor"></div>
  <div class="media-outdoor abs" role="img" aria-label="Photos of an outdoor bootcamp class training on grass"></div>
  <svg class="play abs" width="22" height="24" viewBox="0 0 22 24"><polygon points="1,1 21,12 1,23" fill="#fff"/></svg>
  <a class="media-more abs" href="#" style="color:#fff;text-decoration:none">View more photos and<br>videos &#9656;</a>
</section>

<section class="numbers abs">
  <div class="num-cell num-intro">
    <div class="num-intro-photo" role="img" aria-label="Dark photo of a muscular torso"></div>
    <svg width="28" height="30" viewBox="0 0 28 30" fill="none" stroke="#555" stroke-width="1.4">
      <path d="M3 28 C2 20 4 14 9 11 L12 4 L18 2 L20 6 L16 8 L15 13 C20 12 25 15 26 21 C26 26 20 28 14 28 Z"/>
    </svg>
    <h2>My fit<br>numbers</h2>
  </div>
  <div class="num-cell">
    <div class="num-value">100</div>
    <div class="num-label">I have ideas<br>for training</div>
  </div>
  <div class="num-cell">
    <div class="num-value">20</div>
    <div class="num-label">Nulla pretium tortor<br>a odio sagittis eget</div>
  </div>
  <div class="num-cell">
    <div class="num-value">7</div>
    <div class="num-label">In commodo est quis<br>enim iaculis mattis</div>
  </div>
</section>

<section class="blog abs">
  <h2 class="abs">Read<br>my blog</h2>
  <p class="abs">Lorem ipsum dolor sit amet, consectetur adipiscing elit.<br>Nulla pretium tortor a odio sagittis eget lacinia erat ultricies.</p>
  <div class="blog-art abs" role="img" aria-label="Image of chrome dumbbells"></div>
  <a class="btn btn-white abs" href="#">View my blog</a>
</section>

<footer class="footer abs">
  <nav class="foot-nav abs">
    <a href="#" style="left:0"><sup>01</sup>Home</a>
    <a href="#" style="left:51px"><sup>02</sup>About</a>
    <a href="#" style="left:106px"><sup>03</sup>Services</a>
    <a href="#" style="left:168px"><sup>04</sup>Blog/Videos</a>
    <a href="#" style="left:245px"><sup>05</sup>Contact</a>
  </nav>
  <div class="copyright abs">Copyright © 2016 Voranel.com. All rights reserved.</div>
</footer>

</body>
</html>
```